Auto Mechanic business card

Need a general business card for GearFixer.
Name on card should be 'Roadside Wrench'
Tel # (869) 412 3097
Address is - Palm Lane, Basseterre, St. Kitts
Whatsapp and facebook symbols should be added
On back of card should include services offered
General Repairs
Brakes
Tune Ups
Suspensions
Oil Leaks
Dent repairs
Suspensions
Car Sales
Tyre Repairs
General service
Check Engine Light
Minor Electricals

Target Market(s)

General Population, University students

Industry/Entity Type

Auto Mechanic

Contact Information for Business Card

Roadside Wrench

Requirements
Must have
• 2 Sides

```html
<!DOCTYPE html>
<html lang="en">
<head>
<meta charset="utf-8">
<title>Roadside Wrench – Business Card</title>
<link href="https://fonts.googleapis.com/css2?family=Montserrat:wght@400;500;600;700&display=swap" rel="stylesheet">
<style>
  :root {
    --navy: #0b2f5f;
    --sky: #0099ff;
    --paper: #ffffff;
  }
  * { margin: 0; padding: 0; box-sizing: border-box; }
  html, body {
    width: 1200px; height: 1000px; overflow: hidden;
    background: var(--paper);
    font-family: "Montserrat", Arial, sans-serif;
    color: var(--navy);
  }
  .canvas { position: relative; width: 1200px; height: 1000px; }

  .card-front {
    position: absolute; left: 338px; top: 182px;
    width: 524px; height: 298px;
    border: 4px solid var(--sky);
    background: var(--paper);
  }
  .brand-name {
    position: absolute; left: 0; right: 0; top: 112px;
    text-align: center;
    font-weight: 700; font-size: 31px; letter-spacing: 0.5px;
    color: var(--navy);
  }
  .contact-line {
    position: absolute; left: 0; right: 0; top: 176px;
    display: flex; justify-content: center; align-items: center; gap: 10px;
    font-weight: 700; font-size: 22px; letter-spacing: 0.6px;
  }
  .chat-dot {
    width: 26px; height: 26px; border-radius: 50%;
    border: 3px solid var(--sky);
  }
  .social-square {
    width: 26px; height: 26px; border-radius: 4px;
    background: var(--sky);
  }
  .address {
    position: absolute; left: 0; right: 0; top: 218px;
    text-align: center;
    font-weight: 600; font-size: 16px; letter-spacing: 0.4px;
  }
  .accent-line { position: absolute; left: 0; top: 0; }

  .card-back {
    position: absolute; left: 338px; top: 519px;
    width: 524px; height: 298px;
  }
  .card-back svg { position: absolute; left: 0; top: 0; }
  .services {
    position: absolute; left: 0; right: 0; top: 20px;
    list-style: none; text-align: center;
  }
  .services-title {
    font-weight: 700; font-size: 19px; letter-spacing: 0.3px;
    line-height: 26px; margin-bottom: 0;
  }
  .service {
    font-weight: 500; font-size: 19px; line-height: 26px; letter-spacing: 0.3px;
    display: flex; justify-content: center; align-items: center; gap: 6px;
  }
  .service .dot {
    width: 5px; height: 5px; border-radius: 50%; background: var(--sky);
  }
  .service .bolt { width: 16px; height: 22px; }
</style>
</head>
<body>
<div class="canvas">

  <section class="card-front">
    <div class="brand-name">ROADSIDE WRENCH</div>
    <div class="contact-line">
      <span class="chat-dot"></span>
      <span class="phone">TEL # (869) 412 3097</span>
      <span class="social-square"></span>
    </div>
    <div class="address">PALM LANE, BASSETERRE, ST. KITTS</div>
    <svg class="accent-line" width="516" height="290" viewBox="0 0 516 290">
      <polygon points="90,252 198,258 308,244 426,262 308,248 198,264" fill="var(--sky)"/>
    </svg>
  </section>

  <section class="card-back">
    <svg width="524" height="298" viewBox="0 0 524 298">
      <rect width="524" height="298" fill="var(--sky)"/>
      <clipPath id="inner"><rect x="0" y="4" width="524" height="289"/></clipPath>
      <ellipse cx="262" cy="129" rx="222" ry="230" fill="var(--paper)" clip-path="url(#inner)"/>
    </svg>
    <ul class="services">
      <li class="services-title">GENERAL SERVICE &amp; REPAIRS</li>
      <li class="service"><span class="dot"></span>BRAKES</li>
      <li class="service"><span class="dot"></span>TUNE UPS</li>
      <li class="service"><span class="dot"></span>SUSPENSIONS</li>
      <li class="service"><span class="dot"></span>OIL LEAKS</li>
      <li class="service"><span class="dot"></span>DENT REPAIRS</li>
      <li class="service"><span class="dot"></span>CAR SALES</li>
      <li class="service"><span class="dot"></span>TYRE REPAIRS</li>
      <li class="service"><svg class="bolt" viewBox="0 0 16 22"><polygon points="10,0 2,12 8,12 4,22 14,9 8,9 12,0" fill="var(--sky)"/></svg>CHECK ENGINE LIGHT</li>
      <li class="service"><svg class="bolt" viewBox="0 0 16 22"><polygon points="10,0 2,12 8,12 4,22 14,9 8,9 12,0" fill="var(--sky)"/></svg>MINOR ELECTRICALS</li>
    </ul>
  </section>

</div>
</body>
</html>
```